An anniversary gift for my girlfriend

My girlfriend and I have been dating for almost 2 years. We met online and this has afforded us the really unique opportunity to have the first words we said to each other (the whole conversation, in fact) preserved. We're moving in together in a few months and she doesn't know that I saved the conversation. I've been waiting for this to turn it into something we can hang in our new place.

The only phrase I want to use is:
"Well if you dislike people's knees then I think we'll get along famously"

It's an Nobody Leaves Before Midnight in Portland reference for the curious.

I want the poster to use the words themselves as the art; I'm thinking typography. I'd like it to match her aesthetic, she likes to wear Nora Vell and T. Brisk. Colors shouldn't be anything too "girly". Somewhere I'd like to include the date June 1, 2015. It shouldn't be a major piece of the poster though, just a way to denote the date.

It should fit (and be fully visible in) a 16x20 (inches) frame

Thanks in advance for the work!

Requirements
Must have
• Must use only the words: "Well if you dislike people's knees then I think we'll get along famously"
• I want this to be typography, so making the phrase the center of the poster and the art itself.

```html
<!DOCTYPE html>
<html lang="en">
<head>
<meta charset="utf-8">
<title>Knees — June 1, 2015</title>
<link href="https://fonts.googleapis.com/css2?family=Bodoni+Moda:ital,opsz,wght@0,6..96,400;0,6..96,800;1,6..96,400;1,6..96,700&family=Parisienne&display=swap" rel="stylesheet">
<style>
  :root {
    --paper: #f7f7f3;
    --frame: #111111;
    --ink: #111111;
    --accent: #e8262b;
  }
  html, body {
    margin: 0;
    width: 1200px;
    height: 900px;
    overflow: hidden;
    background: #ffffff;
  }
  .poster {
    position: relative;
    width: 1200px;
    height: 900px;
  }
  .poster-frame {
    position: absolute;
    left: 52px;
    top: 18px;
    width: 1082px;
    height: 850px;
    border: 8px solid var(--frame);
    border-radius: 4px;
    background: var(--paper);
  }
  .phrase {
    position: absolute;
    left: 466px;
    top: 37px;
    width: 283px;
    font-family: "Bodoni Moda", serif;
    font-style: italic;
    font-weight: 700;
    font-size: 25px;
    line-height: 30.4px;
    color: var(--ink);
    text-transform: uppercase;
  }
  .line {
    display: flex;
    justify-content: space-between;
    align-items: baseline;
    height: 30.4px;
    white-space: nowrap;
  }
  .line--indent { padding-left: 10px; }
  .stanza--red { color: var(--accent); }
  .line--light {
    font-style: normal;
    font-weight: 400;
  }
  .initial {
    display: inline-block;
    width: 20px;
    height: 13px;
    margin-right: 2px;
    background: var(--ink);
    vertical-align: 4px;
  }
  .initial--red { background: var(--accent); }
  .small-we {
    font-family: "Bodoni Moda", serif;
    font-style: italic;
    font-weight: 400;
    font-size: 12px;
    text-transform: none;
    vertical-align: 9px;
    margin-right: 1px;
  }
  .small-we--ink { color: var(--ink); }
  .small-we--red { color: var(--accent); }
  .date {
    position: absolute;
    left: 415px;
    top: 568px;
    transform: translate(-50%, -50%) rotate(-90deg);
    font-family: "Parisienne", cursive;
    font-size: 30px;
    color: var(--ink);
    white-space: nowrap;
  }
  .date-day {
    position: absolute;
    left: 390px;
    top: 651px;
    transform: translate(-50%, -50%) rotate(-90deg);
    font-family: "Bodoni Moda", serif;
    font-weight: 800;
    font-size: 30px;
    line-height: 1;
    color: var(--ink);
  }
  .seal {
    position: absolute;
    left: 783px;
    top: 628px;
    width: 86px;
    height: 42px;
    border-radius: 4px;
    background: var(--accent);
  }
</style>
</head>
<body>
<main class="poster">
  <div class="poster-frame"></div>

  <section class="phrase" aria-label="Well if you dislike people's knees then I think we'll get along famously">
    <div class="stanza">
      <div class="line line--indent"><span>Well,</span><span>if</span><span>you</span></div>
      <div class="line"><span>D</span><span>I</span><span>S</span><span>L</span><span>I</span><span>K</span><span>E</span></div>
      <div class="line"><span>P</span><span>E</span><span>O</span><span>P</span><span>L</span><span>E</span><span>’</span><span>S</span></div>
      <div class="line"><span>Knees,</span><span>then</span><span>I</span></div>
      <div class="line"><span>Think</span><span>we’ll</span></div>
      <div class="line"><span>Get</span><span>along</span></div>
      <div class="line"><span>F</span><span>A</span><span>M</span><span>O</span><span>U</span><span>S</span><span>L</span><span>Y</span><span>.</span></div>
    </div>

    <div class="stanza stanza--red">
      <div class="line line--indent"><span><span class="initial" role="img" aria-label="Ornamental initial W"></span>ell,</span><span>if</span><span>you</span></div>
      <div class="line"><span>D</span><span>I</span><span>S</span><span>L</span><span>I</span><span>K</span><span>E</span></div>
      <div class="line"><span>P</span><span>E</span><span>O</span><span>P</span><span>L</span><span>E</span><span>’</span><span>S</span></div>
      <div class="line"><span>Knees,</span><span><span class="initial" role="img" aria-label="Ornamental initial T"></span>hen</span><span>I</span></div>
      <div class="line"><span>Think</span><span><span class="small-we small-we--ink">we</span>’ll</span></div>
      <div class="line"><span>Get</span><span>along</span></div>
      <div class="line"><span>F</span><span>A</span><span>M</span><span>O</span><span>U</span><span>S</span><span>L</span><span>Y</span><span>.</span></div>
    </div>

    <div class="stanza">
      <div class="line line--indent"><span><span class="initial initial--red" role="img" aria-label="Ornamental initial W"></span>ell,</span><span>if</span><span>you</span></div>
      <div class="line"><span>D</span><span>I</span><span>S</span><span>L</span><span>I</span><span>K</span><span>E</span></div>
      <div class="line"><span>P</span><span>E</span><span>O</span><span>P</span><span>L</span><span>E</span><span>’</span><span>S</span></div>
      <div class="line"><span>Knees,</span><span><span class="initial initial--red" role="img" aria-label="Ornamental initial T"></span>hen</span><span>I</span></div>
      <div class="line"><span>Think</span><span><span class="small-we small-we--red">we</span>’ll</span></div>
      <div class="line"><span>Get</span><span>along</span></div>
      <div class="line line--light"><span>F</span><span>A</span><span>M</span><span>O</span><span>U</span><span>S</span><span>L</span><span>Y</span><span>.</span></div>
    </div>
  </section>

  <div class="date">june 2015</div>
  <div class="date-day">1</div>

  <div class="seal" role="img" aria-label="Plain red seal"></div>
</main>
</body>
</html>
```